Brochure Design Project

I need a presentation folder with two inside pages and a pocket on back cover, use use my logo ,
make the cover just using the logo (put it big and centered, then use the logo in the background to fill, read the brief and make it modern, stop trying to make it exactly like the picture I gave as sample please use your talent trust your self
I just uploaded text for presentation folder
Dr's offices and patients

```html
<!DOCTYPE html>
<html lang="en">
<head>
<meta charset="utf-8">
<title>ClearPath Counseling – Folder Inside Spread</title>
<link href="https://fonts.googleapis.com/css2?family=Source+Sans+3:wght@400;600&display=swap" rel="stylesheet">
<style>
  :root {
    --brown: #8a4a1f;
    --brown-deep: #7a3b12;
    --ink: #3b3b3b;
    --ink-soft: #555;
    --page: #ffffff;
    --page-shade: #e4e4e4;
    --stage: #eeeeee;
    --leaf: #8a5a35;
  }
  * { box-sizing: border-box; margin: 0; padding: 0; }
  html, body { width: 1200px; height: 860px; overflow: hidden; }
  body {
    background: var(--stage);
    font-family: "Source Sans 3", sans-serif;
    color: var(--ink);
    position: relative;
  }
  .spread {
    position: absolute;
    left: 22px; top: 35px;
    width: 1156px; height: 790px;
    display: flex;
    box-shadow: 0 4px 14px rgba(0,0,0,.18);
  }
  .page { position: relative; width: 578px; height: 790px; overflow: hidden; }

  /* Front inside */
  .page--front {
    background: linear-gradient(to bottom, var(--page-shade) 0%, #f3f3f3 40%, var(--page) 75%);
  }
  .section-title {
    font-weight: 400;
    font-size: 20px;
    color: var(--brown);
    line-height: 1;
    margin-bottom: 13px;
  }
  .col { position: absolute; z-index: 1; }
  .col--about { left: 44px; top: 48px; width: 210px; }
  .col--services { left: 297px; top: 48px; width: 218px; }
  .col--education { left: 297px; top: 290px; width: 218px; }
  .col--values { left: 44px; top: 552px; width: 222px; }

  .body-copy p {
    font-size: 8.3px;
    line-height: 11.6px;
    text-align: justify;
    margin-bottom: 11px;
    color: var(--ink-soft);
  }
  .bullets { list-style: none; }
  .bullets li {
    position: relative;
    padding-left: 15px;
    font-size: 8.3px;
    line-height: 11.2px;
    margin-bottom: 7px;
    color: var(--ink);
  }
  .bullets--tight li { margin-bottom: 3.4px; }
  .col--values .bullets li { margin-bottom: 10px; text-align: justify; color: var(--ink-soft); }
  .bullets li::before {
    content: "";
    position: absolute;
    left: 1px; top: 2px;
    width: 7px; height: 6px;
    background: var(--leaf);
    border-radius: 0 70% 0 70%;
  }
  .stat-note {
    margin-top: 12px;
    font-size: 8.3px;
    line-height: 11.6px;
    text-align: justify;
  }
  .photo-couple {
    position: absolute;
    left: 250px; top: 500px;
    width: 328px; height: 290px;
    background: linear-gradient(160deg, #c98a6e 0%, #e58aa2 35%, #e9e5e1 70%, #f4f2f0 100%);
    -webkit-mask-image: radial-gradient(ellipse 60% 60% at 60% 55%, #000 45%, transparent 100%);
    mask-image: radial-gradient(ellipse 60% 60% at 60% 55%, #000 45%, transparent 100%);
  }

  /* Back inside */
  .page--back {
    background: linear-gradient(to bottom, var(--page) 0%, var(--page) 45%, #ededed 80%);
  }
  .brand {
    position: absolute;
    top: 112px; left: 0; width: 100%;
    display: flex; align-items: center; justify-content: center; gap: 10px;
  }
  .brand__dot {
    width: 26px; height: 26px; border-radius: 50%;
    background: var(--brown);
  }
  .brand__name {
    font-size: 26px;
    font-weight: 400;
    color: var(--brown);
    line-height: 1;
  }
  .web-address {
    position: absolute;
    top: 189px; left: 0; width: 100%;
    text-align: center;
    font-size: 9.5px;
    letter-spacing: 3.3px;
    color: var(--brown-deep);
  }
  .photo-family { position: absolute; left: 0; top: 0; width: 578px; height: 790px; }
</style>
</head>
<body>
  <main class="spread">
    <section class="page page--front">
      <div class="photo-couple" role="img" aria-label="Photo of a smiling young couple, the woman leaning over the man's shoulders"></div>

      <div class="col col--about body-copy">
        <h2 class="section-title">ClearPath Counseling</h2>
        <p>ClearPath Counseling is a proactive addiction counseling agency dedicated to address health issues in an integrated manner by working with Pain Management Physicians to offer opioid education to prevent substance use and misuse disorders to their Patients. ClearPath Counseling is a resource for Pain Management Clinics to educate and provide prevention and counseling program to patients to reduce the risk of substance use disorders for those patients at risk to pain related substance use disorders.</p>
        <p>ClearPath Counseling will provide education and prevention to individuals who are prescribed medications for health related reasons to prevent possible substance use disorders.</p>
        <p>ClearPath Counseling will receive referrals from pain management clinics to address this growing issue in healthcare.</p>
        <p>ClearPath Counseling services are provided by addiction professionals who are experienced in working in all areas of addiction education and prevention and care.</p>
        <p>Many Pain Management Physicians are interested in reducing risk to their patients and practice from opioid misuse and Increasing Quality Care for their Patients!</p>
        <p>ClearPath Counseling will provide education services and screening to provide patients information to reduce the possible addiction potential.</p>
        <p>ClearPath Counseling will provide education, prevention, screening, assessments, and referrals for those individuals with chronic pain and substance use disorders.</p>
      </div>

      <div class="col col--services">
        <h2 class="section-title">Services Offered</h2>
        <ul class="bullets">
          <li>Pro active opiod education</li>
          <li>Education materials to inform patients about the risk of taking medications inappropriately.</li>
          <li>Prevention services to educate patients about the risk and warning symptoms of substance misuse and abuse</li>
          <li>Screening for potential substance use disorders related to prescribed</li>
          <li>Assessment for substance use disorders related to medical issues and prescribed medications</li>
          <li>Counseling provided by experienced addiction professionals to address substance related misuse and abuse for patients taking prescribed medications.</li>
        </ul>
      </div>

      <div class="col col--education">
        <h2 class="section-title">Opiod Education</h2>
        <ul class="bullets bullets--tight">
          <li>Using Opiods safely</li>
          <li>The Role of Medications</li>
          <li>Opiod Agreements and Contracts</li>
          <li>Responsible Use</li>
          <li>Storing Medication</li>
          <li>Alcohol &amp; Marijuana and Pain Medication</li>
          <li>Over the Counter Medication</li>
          <li>Storing your Medication Safely</li>
        </ul>
        <p class="stat-note">According to the Meridian Pain Research Council More than 76 million Americans are Suffering with Chronic Pain, Pro Active Addiction Counseling is Needed and No One is Providing This Service!</p>
      </div>

      <div class="col col--values">
        <h2 class="section-title">ClearPath Counseling is !</h2>
        <ul class="bullets">
          <li>ClearPath's Dedicated Counselors exude a contagious interest in the life of our patients, within an intimately scaled caring environment that engenders transformative learning</li>
          <li>We'er dedicated to informing and educating lives</li>
          <li>where every patient is treated as a person with individual needs by professional, caring staff</li>
        </ul>
      </div>
    </section>

    <section class="page page--back">
      <div class="brand">
        <span class="brand__dot"></span>
        <span class="brand__name">ClearPath Counseling</span>
      </div>
      <p class="web-address">www.clearpathcounselling.com</p>

      <svg class="photo-family" viewBox="0 0 578 790">
        <defs>
          <linearGradient id="familyTones" x1="0" y1="0" x2="1" y2="0">
            <stop offset="0" stop-color="#b9cf7a"/>
            <stop offset="0.3" stop-color="#d9a88e"/>
            <stop offset="0.6" stop-color="#6f86b5"/>
            <stop offset="0.85" stop-color="#7fae63"/>
            <stop offset="1" stop-color="#cfe3a8"/>
          </linearGradient>
        </defs>
        <path role="img" aria-label="Photo of a happy family of four sitting outdoors in a sunny green meadow"
              d="M0,672 C120,560 300,480 578,492 L578,790 L0,790 Z" fill="url(#familyTones)"/>
        <path d="M0,672 C120,560 300,480 578,492" fill="none" stroke="#8b4513" stroke-width="6"/>
      </svg>
    </section>
  </main>
</body>
</html>
```